Kiosk Coin Venture: Safe and Secure Cash Money

Front of card: LOGO

Back of card:
$$$ FREE ATM PLACEMENT $$$
BENIFITS OF HAVING AN ATM AT YOUR BUSINESS
FREE ATM and BTM (Bitcoin) installation, maintenance, and loading.
Lower card processing fees
Stimulate more traffic.
Ease of access for customers
Maintain customers inside location.
Higher tips and spending

Contact me for more information!
Name: Tobias Merlano
Phone: (512) 638-9071 - Call or Text
Email: Tobias@KioskCoin.example

Contact Information for Business Card

The card should be shape of the logo. Only the back will have all the contact and business details.

Requirements
Must have
• The logo itself will be one side, the card will be the shape of the logo. contact details on back side.

```html
<!DOCTYPE html>
<html lang="en">
<head>
<meta charset="utf-8">
<title>Kiosk Coin Venture – Business Card</title>
<link href="https://fonts.googleapis.com/css2?family=Barlow:wght@300;400;500;700;800&display=swap" rel="stylesheet">
<style>
  :root {
    --bg: #2b2b2d;
    --card-black: #050505;
    --silver-light: #f4f4f4;
    --silver-mid: #c9c9c9;
    --silver-dark: #9a9a9a;
    --ink: #111111;
    --ink-soft: #2a2a2a;
  }
  * { margin: 0; padding: 0; box-sizing: border-box; }
  html, body {
    width: 1200px; height: 800px; overflow: hidden;
    background: var(--bg);
    font-family: "Barlow", sans-serif;
  }
  .stage {
    position: relative; width: 1200px; height: 800px;
    display: flex; align-items: center; justify-content: center; gap: 60px;
  }
  .card {
    position: relative; width: 520px; height: 310px;
    border-radius: 22px; overflow: hidden;
    background: var(--card-black);
    box-shadow: 0 14px 30px rgba(0,0,0,.55);
  }
  .card-back__panel { position: absolute; inset: 0; }
  .card-back__content {
    position: absolute; left: 30px; top: 26px; width: 290px;
    color: var(--ink);
  }
  .headline {
    font-weight: 800; font-size: 22px; letter-spacing: .3px; line-height: 1;
  }
  .subhead {
    font-weight: 700; font-size: 10.5px; letter-spacing: .3px;
    margin-top: 5px; text-transform: uppercase;
  }
  .benefits {
    position: relative; list-style: none; margin-top: 12px; padding-left: 30px;
    font-weight: 400; font-size: 13px; line-height: 15.5px; color: var(--ink-soft);
  }
  .benefits__rail {
    position: absolute; left: 6px; top: 4px; height: 104px;
    border-left: 1.5px dashed var(--ink-soft);
  }
  .benefits__dot {
    position: absolute; left: 0; width: 13px; height: 13px;
    border-radius: 50%; background: var(--ink);
  }
  .contact-name {
    margin-top: 12px; font-weight: 400; font-size: 24px;
    letter-spacing: .5px; text-transform: uppercase; line-height: 1;
  }
  .contact-line {
    display: flex; align-items: center; gap: 8px;
    font-size: 14px; margin-top: 5px; color: var(--ink-soft);
  }
  .contact-line em { font-style: italic; }
  .contact-line--email { font-size: 12px; margin-top: 3px; }
  .contact-line svg { flex: none; }
  .brand-mark {
    position: absolute; display: flex; align-items: center; gap: 10px;
    color: var(--silver-mid); font-weight: 700; text-transform: uppercase;
    letter-spacing: 1px;
  }
  .brand-mark__circle {
    border-radius: 50%; background: var(--silver-mid); flex: none;
  }
  .card-back .brand-mark { right: 30px; top: 40px; font-size: 15px; width: 150px; line-height: 1.1; }
  .card-back .brand-mark__circle { width: 16px; height: 16px; }
  .card-front .brand-mark {
    left: 50%; top: 50%; transform: translate(-50%, -50%);
    font-size: 34px; white-space: nowrap;
  }
  .card-front .brand-mark__circle { width: 30px; height: 30px; }
</style>
</head>
<body>
<main class="stage">

  <section class="card card-back" aria-label="Card back">
    <svg class="card-back__panel" width="520" height="310" viewBox="0 0 520 310" aria-hidden="true">
      <defs>
        <linearGradient id="silverSheen" x1="0" y1="0" x2="1" y2="1">
          <stop offset="0" stop-color="#bdbdbd"/>
          <stop offset=".35" stop-color="#f6f6f6"/>
          <stop offset=".65" stop-color="#d8d8d8"/>
          <stop offset="1" stop-color="#a8a8a8"/>
        </linearGradient>
      </defs>
      <path d="M0 0 H300 Q370 155 300 310 H0 Z" fill="#8c8c8c"/>
      <path d="M0 0 H292 Q360 155 292 310 H0 Z" fill="url(#silverSheen)"/>
    </svg>

    <div class="card-back__content">
      <h1 class="headline">$$$ FREE ATM PLACEMENT $$$</h1>
      <p class="subhead">Benefits of having an ATM at your business</p>
      <ul class="benefits">
        <span class="benefits__rail"></span>
        <span class="benefits__dot" style="top:14px"></span>
        <span class="benefits__dot" style="top:42px"></span>
        <span class="benefits__dot" style="top:70px"></span>
        <span class="benefits__dot" style="top:98px"></span>
        <li>FREE ATM &amp; BTM (Bitcoin)</li>
        <li>installation, maintenance, &amp; loading.</li>
        <li>Lower card processing fees</li>
        <li>Stimulate more traffic.</li>
        <li>Ease of access for customers</li>
        <li>Maintain customers inside location.</li>
        <li>Higher tips &amp; spending</li>
      </ul>
      <p class="contact-name">Tobias Merlano</p>
      <p class="contact-line">
        <svg width="12" height="12" viewBox="0 0 24 24" aria-hidden="true"><path fill="#111" d="M6.6 10.8a15.1 15.1 0 0 0 6.6 6.6l2.2-2.2c.3-.3.7-.4 1-.2 1.1.4 2.3.6 3.6.6.6 0 1 .4 1 1V20c0 .6-.4 1-1 1A17 17 0 0 1 3 4c0-.6.4-1 1-1h3.5c.6 0 1 .4 1 1 0 1.3.2 2.5.6 3.6.1.3 0 .7-.2 1z"/></svg>
        <span>(512) 638-9071 <em>Call Or Text</em></span>
      </p>
      <p class="contact-line contact-line--email">
        <svg width="12" height="10" viewBox="0 0 24 18" aria-hidden="true"><rect x="1" y="1" width="22" height="16" rx="1" fill="#111"/><path d="M1 1l11 9 11-9" stroke="#ddd" stroke-width="1.6" fill="none"/></svg>
        <span>Tobias@KioskCoin.example</span>
      </p>
    </div>

    <div class="brand-mark"><span class="brand-mark__circle"></span><span>Kiosk Coin Venture</span></div>
  </section>

  <section class="card card-front" aria-label="Card front">
    <div class="brand-mark"><span class="brand-mark__circle"></span><span>Kiosk Coin Venture</span></div>
  </section>

</main>
</body>
</html>
```